New brand for digital company - your chance to get creative

We need to create a brand for our new business 'Lanternfish Digital'. Please read the brief below before progressing as we are looking for some quite specific outputs.

Background

We are positioning ourselves as ‘marketing technologists’ - we're helping businesses engage with their customers in the online space.

Our tactics include branding, marketing, online management, and social media, however we are differentiating ourselves by focusing on overall strategy, not just tactics. Our tagline is ‘Online made simple’.

We have stipulated some parameters for the brand but otherwise want designers to exercise their creativity.

Requirements
Must have
• We want to see an entire concept, not just a logo.

```html
<!DOCTYPE html>
<html lang="en">
<head>
<meta charset="utf-8">
<title>Lanternfish Digital – Online made simple</title>
<link rel="stylesheet" href="https://fonts.googleapis.com/css2?family=Yanone+Kaffeesatz:wght@300;400;500&family=Questrial&display=swap">
<style>
  :root {
    --brand-orange: #f0a81c;
    --brand-navy: #2b2f93;
    --brand-blue: #4a4fb8;
    --ink-grey: #474747;
    --copy-blue: #5b5f9e;
    --paper: #ffffff;
    --photo-dark: #2a2a2e;
    --photo-mid: #6b6866;
    --photo-light: #d9d6d2;
  }
  * { margin: 0; padding: 0; box-sizing: border-box; }
  html, body {
    width: 927px; height: 1200px; overflow: hidden;
    background: var(--paper);
  }
  .flyer {
    position: relative;
    width: 927px; height: 1200px;
    overflow: hidden;
    background: var(--paper);
    font-family: "Questrial", sans-serif;
  }
  .top-rule {
    position: absolute; left: 0; top: 0;
    width: 100%; height: 12px;
    background: linear-gradient(to bottom, #8f93d9 0 4px, var(--brand-navy) 4px 12px);
  }
  .data-trail {
    position: absolute; left: 0; top: 0;
    width: 927px; height: 1200px;
  }
  .brand-lockup {
    position: absolute; left: 51px; top: 51px;
    color: var(--ink-grey);
    font-family: "Yanone Kaffeesatz", sans-serif;
    font-weight: 400;
  }
  .brand-square {
    width: 118px; height: 118px;
    margin-left: 70px; margin-bottom: 22px;
    background: var(--brand-orange);
  }
  .brand-name {
    display: block;
    font-size: 64px; line-height: 62px;
    letter-spacing: 0.5px;
  }
  .brand-descriptor {
    display: block;
    font-size: 46px; line-height: 50px;
    letter-spacing: 17px;
  }
  .tagline-band {
    position: absolute; left: 0; top: 331px;
    width: 820px; height: 76px;
    background: linear-gradient(to right, var(--brand-navy) 0%, var(--brand-blue) 30%, rgba(255,255,255,0) 100%);
    border-bottom: 5px solid var(--brand-navy);
    border-image: linear-gradient(to right, var(--brand-navy), rgba(43,47,147,0)) 1;
  }
  .tagline {
    position: absolute; left: 34px; top: 10px;
    color: var(--paper);
    font-family: "Yanone Kaffeesatz", sans-serif;
    font-weight: 400;
    font-size: 50px; line-height: 56px;
  }
  .headline {
    position: absolute; left: 366px; top: 430px;
    color: var(--brand-orange);
    font-family: "Yanone Kaffeesatz", sans-serif;
    font-weight: 500;
    font-size: 92px; line-height: 92px;
    letter-spacing: 3px;
  }
  .intro-copy {
    position: absolute; left: 77px; top: 530px;
    width: 636px;
    color: var(--copy-blue);
    font-size: 23px; line-height: 35px;
    text-align: justify;
    text-indent: 22px;
  }
  .team-photo {
    position: absolute; left: 292px; top: 770px;
    width: 566px; height: 430px;
    background: radial-gradient(ellipse at 50% 30%, var(--photo-light) 0%, var(--photo-mid) 45%, var(--photo-dark) 80%);
    border-radius: 110px 110px 0 0;
  }
</style>
</head>
<body>
<main class="flyer">
  <div class="top-rule"></div>

  <svg class="data-trail" viewBox="0 0 927 1200" role="img" aria-label="Decorative trail of binary digits curving from the brand name down the right edge">
    <defs>
      <linearGradient id="trail-fade" x1="0" y1="0" x2="0" y2="1">
        <stop offset="0" stop-color="#f0a81c" stop-opacity="0.45"/>
        <stop offset="1" stop-color="#f0a81c" stop-opacity="0.15"/>
      </linearGradient>
    </defs>
    <path d="M370 175 C 560 150, 760 200, 800 330 C 850 480, 870 700, 860 1060" fill="none" stroke="url(#trail-fade)" stroke-width="34" stroke-linecap="round"/>
  </svg>

  <header class="brand-lockup">
    <div class="brand-square"></div>
    <span class="brand-name">LANTERNFISH</span>
    <span class="brand-descriptor">DIGITAL</span>
  </header>

  <div class="tagline-band">
    <p class="tagline">Online made simple</p>
  </div>

  <h1 class="headline">LOREM IPSUM</h1>

  <p class="intro-copy">We are positioning ourselves as ‘marketing technologists’ we’re helping businesses engage with their customers in the online space. Our tactics include branding, marketing online management, and social media, however we are differentiating ourselves by focusing on overall strategy, not just tactics. Our tagline is ‘Online made simple’.</p>

  <div class="team-photo" role="img" aria-label="Group photograph of the five-person team standing together in dark casual clothing"></div>
</main>
</body>
</html>
```